Youth Education Program for WLC

Looking for a high-end slick looking design for power-point and/or PDF. Quick turnaround of a Presentation of 10 slides for a meeting for an educational youth program. Information and recommended images will be provided for each slide. Each Slide other than cover should have a logo, header, footer, and page number. Design should be simple and modern with either graphic examples or images. Less is more. Websites for company is http://brightarcademy.example/ and other images can be found on korvanmedia.example or you can use stock imagery you feel is good.
Colors
Designer to choose colors to be used in the design.
Look and feel
Each slider illustrates characteristics of the customer's brand and the style your logo design should communicate.

```html
<!DOCTYPE html>
<html lang="en">
<head>
<meta charset="utf-8">
<title>Youth Education Program for WLC – Slides 6-10</title>
<link rel="stylesheet" href="https://fonts.googleapis.com/css2?family=Archivo+Black&family=Source+Sans+3:wght@400;600;700&display=swap">
<style>
  :root{
    --canvas:#bec0ca;
    --orange-red:#e9441a;
    --orange:#f59b22;
    --green:#8cc63f;
    --green-dark:#6f9b2c;
    --lime:#e2ee1b;
    --cyan:#2ec8ea;
    --cyan-soft:#cdf0f9;
    --cyan-head:#27aede;
    --blue:#1b8acb;
    --ink:#2a2a2a;
    --white:#ffffff;
  }
  *{margin:0;padding:0;box-sizing:border-box}
  html,body{width:1200px;height:3016px;overflow:hidden}
  body{background:var(--canvas);font-family:"Source Sans 3",sans-serif;color:var(--ink);position:relative}
  .slide{position:absolute;background:var(--white);overflow:hidden;box-shadow:0 14px 26px rgba(40,40,60,.35)}
  .slide-art{position:absolute;left:0;top:0}
  .slide-title{position:absolute;font-family:"Archivo Black",sans-serif;color:var(--white);font-size:20px;line-height:22px;letter-spacing:.4px}
  .slide-title.right{text-align:right}
  .copy{position:absolute;font-size:11.3px;line-height:15.2px}
  .copy p{margin-bottom:15.2px}
  .copy p.tight{margin-bottom:0}
  .copy .h-green{color:var(--green-dark);font-weight:600;display:block}
  .copy .h-cyan{color:var(--cyan-head);font-weight:600;display:block}
  .page-num{position:absolute;width:32px;height:32px;border-radius:50%;font-size:15px;line-height:32px;text-align:center}
  .page-num.green{background:var(--green);color:var(--white)}
  .page-num.orange{background:#f7941d;color:var(--white)}
  .page-num.white{background:var(--white);color:var(--ink)}
  ul.dot{list-style:none}
  ul.dot li{position:relative;padding-left:8px}
  ul.dot li::before{content:"";position:absolute;left:0;top:6px;width:4px;height:4px;border-radius:50%;background:var(--cyan-head)}
  ul.dot.greenbul li::before{background:var(--green);width:5px;height:5px;top:5px}
  ul.dot.greenbul li{padding-left:11px}
  .col-title{font-weight:600}
  .classroom-label{position:absolute;color:var(--white);font-weight:600;font-size:19px;line-height:22px}
  .modules{font-size:9.4px;line-height:13.1px}
  .modules p{margin-bottom:13.1px}
  .version-label{position:absolute;left:497px;top:2920px;width:276px;text-align:center;color:var(--white);font-weight:700;font-size:40px;line-height:48px}
</style>
</head>
<body>

<!-- Slide 5 : Solving the problem -->
<section class="slide" style="left:190px;top:94px;width:869px;height:488px">
  <svg class="slide-art" width="869" height="488" viewBox="0 0 869 488">
    <defs>
      <linearGradient id="orangeA" x1="0" y1="0" x2="0" y2="1"><stop offset="0" stop-color="#e9441a"/><stop offset="1" stop-color="#f7a322"/></linearGradient>
      <linearGradient id="headA" x1="0" y1="0" x2="1" y2="0"><stop offset="0" stop-color="#2ec8ea"/><stop offset="1" stop-color="#1b8acb"/></linearGradient>
      <linearGradient id="footA" x1="0" y1="0" x2="1" y2="0"><stop offset="0" stop-color="#8cc63f"/><stop offset="1" stop-color="#b9d632"/></linearGradient>
      <linearGradient id="photoA" x1="0" y1="0" x2="0" y2="1"><stop offset="0" stop-color="#c99a7c"/><stop offset=".5" stop-color="#2d4f96"/><stop offset="1" stop-color="#1f2f66"/></linearGradient>
    </defs>
    <rect x="0" y="476" width="869" height="12" fill="url(#footA)"/>
    <polygon points="0,0 86,0 275,488 0,488" fill="url(#orangeA)"/>
    <polygon points="88,60 96,60 287,488 279,488" fill="var(--green)"/>
    <polygon points="361,14 869,14 869,76 395,76" fill="url(#headA)"/>
    <line x1="828" y1="55" x2="861" y2="55" stroke="#fff" stroke-width="2"/>
    <rect x="0" y="200" width="165" height="288" fill="url(#photoA)" role="img" aria-label="Photo of a basketball player holding a ball"/>
  </svg>
  <div class="slide-title right" style="right:56px;top:22px">SOLVING THE PROBLEM<br>Self Regulation Skills</div>
  <div class="copy" style="left:208px;top:80px;width:630px">
    <p>Students show higher school readiness because they are physically healthy, genuinely respect class rules, are less likely to be off task, are more self-reliant and have a more positive attitude towards learning<br>-Teachers spend less time monitoring and responding to negative student behaviour<br>-It is flexible; can be administered to target individual student behaviors depending on their abilities and needs</p>
    <p>While these skills are essential tools for lifelong learning, they are often not explicitly taught, leading to distinct populations of students who lack independence, motivation, persistence and a positive sense of wellbeing.</p>
    <p class="tight"><span class="h-green">Why use Self-Regulation?</span>Self-regulation is desirable because of the effects that it has on educational and behavioral outcomes. The use of Self-Regulation techniques are a way to actively engage otherwise passive students in their academic instruction. Students need to view learning as an activity that they do for themselves in a proactive manner, rather than viewing learning as a covert event that happens to them as a result of instruction (Halvorsen, 2001). Allowing students to take a more active role in their education puts students in the driver's seat and in charge.</p>
  </div>
  <div class="copy" style="left:317px;top:300px;width:535px">
    <p><span class="h-cyan">SOFT SKILLS</span>What are soft skills?<br>Experts broadly define soft skills as a set of non-technical, professional abilities such as communication, interpersonal, and customer service skills, as well as personal traits such as integrity and responsibility that employees need to secure employment and succeed in the workplace</p>
    <p class="tight"><span class="h-cyan">Importance of Soft Skills</span>&nbsp;A 2016 Ledger Business Wire Report stated employers are facing Soft Skills gap in their workers.<br>• The reports assessment was that Soft Skills are being bred out of our culture. They are:<br>○ Being de-emphasized in the family<br>○ Devalued in the education system.</p>
  </div>
  <div class="page-num green" style="left:19px;top:439px">5</div>
</section>

<!-- Slide 6 : Curriculum focus -->
<section class="slide" style="left:190px;top:632px;width:869px;height:492px">
  <svg class="slide-art" width="869" height="492" viewBox="0 0 869 492">
    <defs>
      <linearGradient id="limeB" x1="0" y1="0" x2="0" y2="1"><stop offset="0" stop-color="#e6ef1a"/><stop offset="1" stop-color="#7cc242"/></linearGradient>
      <linearGradient id="headB" x1="0" y1="0" x2="1" y2="0"><stop offset="0" stop-color="#1b8acb"/><stop offset="1" stop-color="#2ec8ea"/></linearGradient>
      <linearGradient id="photoB" x1="0" y1="0" x2="1" y2="1"><stop offset="0" stop-color="#4a6fa8"/><stop offset=".5" stop-color="#ef7a2c"/><stop offset="1" stop-color="#5a3b8c"/></linearGradient>
    </defs>
    <rect x="0" y="480" width="869" height="12" fill="var(--green)"/>
    <polygon points="842,0 869,0 869,492 540,492" fill="url(#limeB)"/>
    <polygon points="0,15 507,15 483,80 0,80" fill="url(#headB)"/>
    <line x1="4" y1="44" x2="39" y2="44" stroke="#fff" stroke-width="2"/>
    <rect x="39" y="94" width="602" height="173" rx="14" fill="var(--cyan-soft)"/>
    <polygon points="683,277 869,277 869,386 652,386" fill="url(#photoB)" role="img" aria-label="Photo of a coach high-fiving young players in a gym"/>
  </svg>
  <div class="slide-title" style="left:54px;top:26px">SOLVING THE PROBLEM<br>Self Regulation Skills</div>
  <div class="copy" style="left:52px;top:101px;width:290px">
    <span class="h-cyan">CURRICULUM FOCUS</span>
    <div class="col-title" style="padding-left:8px">Interpersonal &amp; Social Skills for the Workplace</div>
    <ul class="dot">
      <li>Workplace etiquette and protocol</li>
      <li>Managing relationships</li>
      <li>Understanding the feelings of others</li>
      <li>Cooperating with others</li>
      <li>Great Attitude</li>
      <li>Showing respect</li>
      <li>Appropriate contact</li>
      <li>Effective communication</li>
    </ul>
  </div>
  <div class="copy" style="left:341px;top:116px;width:295px">
    <div class="col-title">Soft and Transferable Skills you need to be successful:</div>
    <ul class="dot" style="padding-left:8px">
      <li>Leadership</li>
      <li>Teamwork</li>
      <li>Communication</li>
      <li>Problem Solving</li>
      <li>Work Ethic</li>
      <li>Flexibility/Adaptability</li>
      <li>Interpersonal Skills</li>
    </ul>
  </div>
  <div class="copy" style="left:52px;top:284px;width:560px">
    <div class="col-title">Our program is designed to produce outcomes that will:</div>
    <ul class="dot greenbul">
      <li>Equip participants to gain meaningful careers that offer advancement, satisfaction and self-sufficiency.</li>
      <li>Instill in them a positive attitude about their abilities and future working in a particular industry, or the opportunities to grow into another.</li>
      <li>Give them the capacity to identify and avoid unduly risky behaviors and activities.</li>
      <li>Teach them how to recognize and use the transferable, or core skills acquired through athletics to succeed in a wide range of situations and jobs.</li>
      <li>Prepare them to be willing and able to give back to their community through volunteerism.</li>
      <li>Facilitate online interactions between teachers, students, coaches, student-athletes and parents.</li>
      <li>Prevent inappropriate social behavior like "persistent disobedience, aggression, and temper tantrums," which can escalate to more severe problems as students age</li>
    </ul>
  </div>
  <div class="page-num white" style="left:818px;top:442px">6</div>
</section>

<!-- Slide 7 : Sample program -->
<section class="slide" style="left:186px;top:1179px;width:873px;height:489px">
  <svg class="slide-art" width="873" height="489" viewBox="0 0 873 489">
    <defs>
      <linearGradient id="orangeC" x1="0" y1="0" x2="0" y2="1"><stop offset="0" stop-color="#e9441a"/><stop offset="1" stop-color="#f7a322"/></linearGradient>
      <linearGradient id="headC" x1="0" y1="0" x2="1" y2="0"><stop offset="0" stop-color="#2ec8ea"/><stop offset="1" stop-color="#1b8acb"/></linearGradient>
      <linearGradient id="footC" x1="0" y1="0" x2="1" y2="0"><stop offset="0" stop-color="#8cc63f"/><stop offset="1" stop-color="#b9d632"/></linearGradient>
      <linearGradient id="photoC" x1="0" y1="0" x2="0" y2="1"><stop offset="0" stop-color="#3a3a3a"/><stop offset=".6" stop-color="#1d4f78"/><stop offset="1" stop-color="#6b4a35"/></linearGradient>
    </defs>
    <rect x="0" y="477" width="873" height="12" fill="url(#footC)"/>
    <polygon points="0,0 60,0 270,489 0,489" fill="url(#orangeC)"/>
    <polygon points="70,40 78,40 287,489 279,489" fill="var(--green)"/>
    <polygon points="360,18 873,18 873,80 394,80" fill="url(#headC)"/>
    <line x1="829" y1="44" x2="864" y2="44" stroke="#fff" stroke-width="2"/>
    <g fill="none" stroke="#fff" stroke-width="3" stroke-linejoin="round">
      <rect x="36" y="254" width="64" height="42"/>
      <polyline points="58,280 72,268 84,276 94,262"/>
      <circle cx="48" cy="270" r="5"/>
      <circle cx="52" cy="307" r="5"/>
      <circle cx="68" cy="307" r="5"/>
      <circle cx="84" cy="307" r="5"/>
      <line x1="38" y1="320" x2="98" y2="320"/>
    </g>
    <rect x="680" y="282" width="160" height="195" rx="10" fill="url(#photoC)" role="img" aria-label="Photo of hands holding a tablet showing the learning portal"/>
  </svg>
  <div class="slide-title right" style="right:58px;top:22px">SAMPLE PROGRAM<br>A Day in the Life</div>
  <div class="classroom-label" style="left:30px;top:332px">CLASSROOM<br>SETTING<br>25-30 students<br>1.5-2 hours per</div>
  <div class="copy" style="left:209px;top:103px;width:640px">
    <p><span class="h-green">THE BRIGHT ARC U TRAINING CURRICULUM/PROGRAM</span>The Bright Arc U training curriculum/program is a comprehensive, interactive and gamified program that combines a structured curriculum, classroom learning and a powerful ePortal to teach professional and personal "soft skills" to student scholars and student athletes.<br>We are fusing tech and tradition to teach the vital life skills that aren't taught in elementary, junior or high schools.</p>
    <p class="tight">Studies have shown that while many young and underprivileged teens and adults struggle in a typical classroom environment, most have developed a strong affinity for technology through the use of mobile phones and video games – and to some degree, computers. This program uses technology/gamification and classical training to cast the widest educational net possible, so students can combine the two environments – online and offline – to boost their health and strength knowledge, self-regulatory skills, prepare for the workplace, and so much more.</p>
  </div>
  <div class="copy" style="left:280px;top:300px;width:380px">
    <p class="tight">The components of the Bright Arc U program are the curriculum (designed for the classroom) and the ePortal / mobile app which will be used for pre and post testing and gamified competition based challenges/activities. The gamification angle (earn badges and points for mastering certain skills, for instance) makes learning fun and rewarding.<br>We will present consistent messaging and give teachers, coaches, parents and students a roadmap to success to help them become productive learners and earners.</p>
  </div>
  <div class="page-num green" style="left:18px;top:442px">7</div>
</section>

<!-- Slide 8 : Sample module offerings -->
<section class="slide" style="left:193px;top:1715px;width:872px;height:489px">
  <svg class="slide-art" width="872" height="489" viewBox="0 0 872 489">
    <defs>
      <linearGradient id="headD" x1="0" y1="0" x2="1" y2="0"><stop offset="0" stop-color="#1b8acb"/><stop offset="1" stop-color="#2ec8ea"/></linearGradient>
      <radialGradient id="photoD" cx=".5" cy=".45" r=".6"><stop offset="0" stop-color="#5b3a2c"/><stop offset=".6" stop-color="#1f4d3a"/><stop offset="1" stop-color="#5e6a70"/></radialGradient>
    </defs>
    <rect x="0" y="477" width="872" height="12" fill="var(--green)"/>
    <polygon points="749,0 872,0 872,489 603,489" fill="var(--blue)"/>
    <polygon points="739,0 749,0 603,489 593,489" fill="var(--green)"/>
    <polygon points="0,14 635,14 609,74 0,74" fill="url(#headD)"/>
    <line x1="4" y1="44" x2="39" y2="44" stroke="#fff" stroke-width="2"/>
    <circle cx="665" cy="328" r="131" fill="url(#photoD)" role="img" aria-label="Photo of a professional basketball player holding a ball"/>
  </svg>
  <div class="slide-title" style="left:57px;top:33px">SAMPLE MODULE OFFERINGS</div>
  <div class="copy modules" style="left:59px;top:94px;width:300px">
    <span class="h-green">Bright Arc WIN ALL FOUR</span>
    <p>The Recruiting Process Begins<br>Divisions and Classifications of Competition<br>Athletic Scholarships<br>Maximum Number of Scholarships per Sport<br>When to Commit?<br>Roles of Individuals<br>Your Coach<br>Your Guidance Counselor<br>The College Recruiter<br>NCAL ELIGIBILITY CENTER<br>NCAL DIVISION I ACADEMIC REQUIREMENTS<br>NCAL DI Sliding Scale<br>NCAL DIVISION II ACADEMIC REQUIREMENTS<br>NCAL DII Sliding Scale<br>NCAL DIII</p>
    <p style="width:420px">Korvan Student Athlete Development Series &nbsp;*Additional modules offering based on need<br>1.&nbsp;&nbsp; First Impressions<br>2.&nbsp;&nbsp; Mastering Organizational, Study and Test Taking Skills<br>3.&nbsp;&nbsp; Responsible Decision Making<br>4.&nbsp;&nbsp; Transitioning from High School to College<br>5.&nbsp;&nbsp; Beyond Athletics</p>
    <p class="tight">Additional Offerings<br>Athletic Director Workshops<br>Facilitator Workshops<br>Parent Workshops</p>
  </div>
  <div class="copy modules" style="left:351px;top:94px;width:290px">
    <span class="h-green">What is YOUR Goal?</span>
    <p class="tight" style="margin-top:13.1px">Bright Arc U Health, Strength and Nutrition<br>This program covers the gamut of Nutrition and Strength training knowledge based concepts. The course is categorized as follows:<br>The Basics of a Nutrition and Strength Program<br>Putting The Basics To Use<br>Percentages<br>Goal Setting<br>Sports Nutrition<br>PED's And Supplements<br>Conditioning<br>Plyometrics<br>Flexibility</p>
  </div>
  <div class="page-num orange" style="left:821px;top:438px">8</div>
</section>

<!-- Slide 9 : What makes us different -->
<section class="slide" style="left:193px;top:2300px;width:893px;height:501px">
  <svg class="slide-art" width="893" height="501" viewBox="0 0 893 501">
    <defs>
      <linearGradient id="limeE" x1="0" y1="0" x2="0" y2="1"><stop offset="0" stop-color="#e6ef1a"/><stop offset="1" stop-color="#7cc242"/></linearGradient>
      <linearGradient id="headE" x1="0" y1="0" x2="1" y2="0"><stop offset="0" stop-color="#1b8acb"/><stop offset="1" stop-color="#2ec8ea"/></linearGradient>
      <linearGradient id="photoE" x1="0" y1="0" x2="0" y2="1"><stop offset="0" stop-color="#6a4330"/><stop offset=".4" stop-color="#e9e9ef"/><stop offset="1" stop-color="#2a2d36"/></linearGradient>
    </defs>
    <rect x="0" y="489" width="893" height="12" fill="var(--green)"/>
    <polygon points="858,0 893,0 893,501 610,501" fill="url(#limeE)"/>
    <polygon points="0,15 521,15 497,76 0,76" fill="url(#headE)"/>
    <line x1="4" y1="45" x2="41" y2="45" stroke="#fff" stroke-width="2"/>
    <rect x="695" y="199" width="198" height="302" fill="url(#photoE)" role="img" aria-label="Photo of a former pro player in shirt and tie holding a basketball"/>
  </svg>
  <div class="slide-title" style="left:66px;top:34px">WHAT MAKES US DIFFERENT</div>
  <div class="copy" style="left:23px;top:92px;width:665px;font-size:11px;line-height:14.8px">
    <p style="margin-bottom:14.8px">Former Professional Athletes are sharing their skills and experiences within the community:<br>●Many of the retired WLC players were successful because they were willing to push themselves well beyond the limits of their peers.<br>●They were also organized and able to successfully balance their academic, athletic and social lives.<br>●They Excel at Time Management (Experience in scenarios</p>
    <p style="margin-bottom:14.8px">From balancing rigorous practice schedules, classes, homework, tournaments and travel, they are pros at time management and prioritization)<br>●We believe we can apply these Soft and Life skills in the academic setting by showing students how to develop a sustained system or routine and recognize triggers that need to be addressed and avoided to ensure success<br>●Many were able to recognize and use the transferable, or core skills acquired through athletics to succeed in a wide range of business and other opportunities after retirement from the WLC.<br>●Assembling a team of professionals who are knowledgeable in the fields of education, web based learning, strength and conditioning training, sports psychology, academics, and coaching, and who have real world experience with the challenges and opportunities of being a student athlete.<br>●We have found that most curriculum on the market are based on the experiences of the developer. The Korvan College Career and Life readiness curriculum is extensively researched, culturally responsive and based on best practices such as the 5E's of Sequential Learning (Engage, Explore, Explain, Elaborate, Evaluate)<br>●We embed soft and life skills that also addresses social emotional (SEL) skills within the content areas in a way that eliminates the question from participants, "When are we going to ever use this stuff?"<br>●Soft skills and life skills are done interactively within the skills used to build the body for athletes; thus we are working to create "The Total Student Athlete".</p>
    <p class="tight">The sustainability factor connects to retired WLC players willing to "check &amp; connect" with participants.<br>Ultimately the Bright Arc U program open doors for the retired WLC innovative leaders who are capable and<br>committed to giving back to the community as well as civically engaged.</p>
  </div>
  <div class="page-num white" style="left:840px;top:449px">9</div>
</section>

<div class="version-label">V2 (SLIDE 6-10)</div>

</body>
</html>
```